Social Media Graphics - Harbor Climb REVISED

Create 6-7 individual social media graphics (square size) to encourage folks to join our online course called:

The Lantern Ledger Plan
How to Launch a Multi-Million Business From Scratch
Sign Up Today!

IMPORTANT: Make the largest and most prominent text on the graphic be: How to Launch a Multi-Million Business From Scratch

For the color scheme of the graphics, let's try a blue color palette; make sure the graphics appeal to both men and women

Make sure each graphic contains 1 of the 3 pics attached (crop pic as needed); and make sure one of the graphics is all TEXT only.

Target Market(s)

men and women looking to start a business

Industry/Entity Type

Entrepreneurship

Colors
0054AA
0677BA
7BADD7
CADEEF
E8F1F8

Requirements
Must have
• All the text and use the 3 pics provided; one graphic can be all text; Simple, modern design that's easy to read

```html
<!DOCTYPE html>
<html lang="en">
<head>
<meta charset="UTF-8">
<title>The Lantern Ledger Plan – Sign Up</title>
<link rel="stylesheet" href="https://fonts.googleapis.com/css2?family=Oswald:wght@500;600;700&display=swap">
<style>
  :root {
    --navy: #0d2a4a;
    --royal: #0054aa;
    --mid: #0677ba;
    --sky: #7badd7;
    --pale: #cadeef;
    --ice: #e8f1f8;
    --yellow: #fff200;
    --white: #ffffff;
  }
  * { margin: 0; padding: 0; box-sizing: border-box; }
  html, body { width: 1200px; height: 1200px; overflow: hidden; }
  body { font-family: "Oswald", "Arial Narrow", sans-serif; background: var(--royal); }

  .poster {
    position: relative;
    width: 1200px;
    height: 1200px;
    overflow: hidden;
    background: radial-gradient(circle at 50% 55%, #0b63bd 0%, var(--royal) 55%, #0a4590 100%);
  }

  .backdrop-money {
    position: absolute;
    left: 0; top: 160px;
    width: 620px; height: 520px;
    background: radial-gradient(ellipse at 30% 40%, rgba(123,173,215,0.35), rgba(0,84,170,0) 70%);
  }
  .backdrop-clock {
    position: absolute;
    right: 0; top: 250px;
    width: 520px; height: 560px;
    background: radial-gradient(circle at 70% 45%, rgba(123,173,215,0.3), rgba(0,84,170,0) 68%);
  }

  .title-band {
    position: absolute;
    left: 0; top: 0;
    width: 1200px; height: 106px;
    background: var(--navy);
    border-bottom: 5px solid var(--mid);
    display: flex;
    align-items: center;
    justify-content: center;
    font-weight: 700;
    font-size: 62px;
    letter-spacing: 1px;
    text-transform: uppercase;
    line-height: 1;
  }
  .title-band .accent { color: var(--yellow); }
  .title-band .soft { color: var(--sky); margin-left: 16px; }

  .headline {
    position: absolute;
    left: 0; top: 128px;
    width: 1200px;
    text-align: center;
    text-transform: uppercase;
    font-weight: 600;
    font-size: 102px;
    line-height: 95px;
    letter-spacing: 1px;
    color: var(--white);
  }
  .headline .highlight { color: var(--yellow); }

  .hosts-photo {
    position: absolute;
    left: 228px; top: 433px;
    width: 783px; height: 767px;
    border-radius: 280px 280px 0 0;
    background: linear-gradient(180deg, #1a3d66 0%, #8a3a4a 60%, #c7364f 100%);
  }

  .cta {
    position: absolute;
    left: 367px; top: 1058px;
    width: 464px; height: 111px;
    background: var(--navy);
    border-top: 4px solid var(--mid);
    border-radius: 18px;
    display: flex;
    align-items: center;
    justify-content: center;
    color: var(--white);
    font-weight: 600;
    font-size: 46px;
    text-transform: uppercase;
    letter-spacing: 1px;
  }
</style>
</head>
<body>
  <main class="poster">
    <div class="backdrop-money" role="img" aria-label="Faded stacks of dollar bills"></div>
    <div class="backdrop-clock" role="img" aria-label="Faded pocket watch clock face"></div>

    <header class="title-band">
      <span class="accent">The Lantern Ledger</span><span class="soft">Plan</span>
    </header>

    <h1 class="headline">
      How to Launch a<br>
      <span class="highlight">Multi-Million Business</span><br>
      From Scratch
    </h1>

    <div class="hosts-photo" role="img" aria-label="Photo of the two smiling course hosts, a woman in a pink dress and a man in a black jacket"></div>

    <div class="cta">Sign Up Today!</div>
  </main>
</body>
</html>
```